We want a hot New Design for our IT company Web Site

We have a basic website with some general information and lots of mostly words and generic pictures we want to make it look and feel a lot more modern and slick. The site needs to work on mobile devices as well as desktops.

Target Market(s)

Business customers

Industry/Entity Type

It Company

Coding

Coded - Design and coding required

Number of Pages Required

5+ page

Requirements
Must have
• Sleek new Design making it look and feel more modern and less boring
Nice to have
• If it can have a better flow to it rather then have the std Drop down menus it has now.

```html
<!DOCTYPE html>
<html lang="en">
<head>
<meta charset="utf-8">
<title>Norvale Tech Group — IT Services</title>
<link href="https://fonts.googleapis.com/css2?family=Roboto:wght@400;500;700;900&display=swap" rel="stylesheet">
<style>
:root{
  --blue:#1a6fc4;
  --blue-dark:#0d4f96;
  --navy:#0b2a4a;
  --ink:#333a42;
  --muted:#7b828a;
  --line:#d9dde2;
  --panel:#eef0f3;
  --white:#ffffff;
  --footer-ink:#555c63;
}
*{box-sizing:border-box;margin:0;padding:0}
html,body{width:781px;height:1200px;overflow:hidden}
body{font-family:"Roboto",Arial,sans-serif;color:var(--ink);background:var(--white);position:relative}

/* header */
.site-header{position:absolute;left:0;top:0;width:781px;height:30px;background:var(--white);display:flex;align-items:center;padding:0 12px 0 18px}
.brand{display:flex;align-items:center;gap:6px;color:var(--blue);font-weight:700;font-size:11px;letter-spacing:.3px}
.brand-dot{width:10px;height:10px;background:var(--blue)}
.main-nav{margin-left:auto;display:flex;gap:0;align-items:center}
.main-nav a{font-size:6.5px;font-weight:500;color:var(--ink);text-decoration:none;padding:0 9px;letter-spacing:.3px}
.main-nav a.active{color:var(--blue)}
.social{display:flex;gap:4px;margin-left:10px}
.social span{width:11px;height:11px;border:1px solid #9aa1a8;border-radius:50%}

/* hero */
.hero{position:absolute;left:0;top:30px;width:781px;height:348px;overflow:hidden}
.hero-bg{position:absolute;inset:0;background:
  radial-gradient(ellipse at 55% 45%,#5f8fbf 0%,#2e5f92 35%,#143a66 70%,#0a2444 100%)}
.hero-content{position:absolute;left:0;right:0;top:138px;text-align:center;color:var(--white)}
.hero-title{font-size:26px;font-weight:900;letter-spacing:1.5px}
.hero-text{width:430px;margin:12px auto 0;font-size:8px;line-height:1.45}
.hero-arrow{position:absolute;top:160px;width:14px;height:24px}
.hero-arrow.prev{left:10px}.hero-arrow.next{right:10px}
.hero-dots{position:absolute;top:295px;left:0;right:0;display:flex;justify-content:center;gap:4px}
.hero-dots span{width:5px;height:5px;border-radius:50%;background:rgba(255,255,255,.55)}
.hero-dots span.on{background:var(--white)}

/* services */
.services{position:absolute;left:0;top:378px;width:781px;height:554px;background:var(--panel)}
.service-card{position:absolute;width:362px;height:230px;background:var(--white)}
.service-card.c1{left:18px;top:34px}
.service-card.c2{left:400px;top:34px}
.service-card.c3{left:18px;top:305px}
.service-card.c4{left:400px;top:305px}
.card-head{height:26px;display:flex;align-items:center;border-bottom:2px solid var(--blue)}
.card-icon{width:34px;height:26px;background:var(--blue);display:flex;align-items:center;justify-content:center;clip-path:polygon(0 0,100% 0,80% 100%,0 100%)}
.card-title{margin-left:8px;font-size:9px;font-weight:700;color:var(--blue-dark);letter-spacing:.3px}
.card-photo{height:105px}
.c1 .card-photo{background:linear-gradient(135deg,#c8d2dc,#8fa3b8 55%,#55718f)}
.c2 .card-photo{background:linear-gradient(135deg,#a9c4e0,#4d7fb5 55%,#1f4b80)}
.c3 .card-photo{background:linear-gradient(135deg,#3b7cc7,#1c4f94 55%,#0d2f63)}
.c4 .card-photo{background:linear-gradient(135deg,#7fa2c7,#3d6a9c 55%,#20406b)}
.card-text{padding:8px 10px 0;font-size:6.8px;line-height:1.55;color:var(--muted)}
.card-link{display:block;padding:8px 10px 0;font-size:6.5px;font-weight:700;color:var(--blue);text-decoration:none;letter-spacing:.3px}

/* blog */
.blog{position:absolute;left:0;top:932px;width:781px;height:160px;overflow:hidden}
.blog-bg{position:absolute;inset:0;background:linear-gradient(180deg,#2b2f34,#181b1f 60%,#24282d)}
.blog-content{position:absolute;left:0;right:0;top:30px;text-align:center;color:var(--white)}
.blog-title{font-size:15px;font-weight:700;letter-spacing:.8px}
.blog-text{width:470px;margin:10px auto 0;font-size:7px;line-height:1.5;color:#d2d5d9}
.blog-link{display:inline-block;margin-top:10px;font-size:6.5px;font-weight:700;color:var(--white);text-decoration:none;letter-spacing:.3px}
.blog-arrow{position:absolute;top:68px;width:12px;height:20px}
.blog-arrow.prev{left:14px}.blog-arrow.next{right:14px}

/* footer */
.site-footer{position:absolute;left:0;top:1092px;width:781px;height:108px;background:var(--white);text-align:center}
.footer-nav{margin-top:38px;display:flex;justify-content:center}
.footer-nav a{font-size:6.5px;font-weight:500;color:var(--ink);text-decoration:none;padding:0 9px;letter-spacing:.3px}
.footer-info{margin-top:8px;font-size:5.8px;line-height:1.6;color:var(--footer-ink)}
</style>
</head>
<body>

<header class="site-header">
  <div class="brand"><span class="brand-dot"></span>Norvale Tech Group</div>
  <nav class="main-nav">
    <a href="#" class="active">HOME</a>
    <a href="#">ABOUT US</a>
    <a href="#">SERVICES</a>
    <a href="#">BLOG</a>
    <a href="#">CONTACT US</a>
  </nav>
  <div class="social"><span></span><span></span><span></span></div>
</header>

<section class="hero">
  <div class="hero-bg" role="img" aria-label="Blue technology background with a world map and network connection lines"></div>
  <div class="hero-content">
    <div class="hero-title">NORVALE TECH GROUP</div>
    <p class="hero-text">Norvale Tech Group offers technology consulting, managed IT services and a resilient cloud platform for the SME sector. With offices in Brisbane and Melbourne, we specialise in meeting the environmental needs of your business.</p>
  </div>
  <svg class="hero-arrow prev" viewBox="0 0 14 24"><polyline points="11,2 3,12 11,22" fill="none" stroke="#fff" stroke-width="2"/></svg>
  <svg class="hero-arrow next" viewBox="0 0 14 24"><polyline points="3,2 11,12 3,22" fill="none" stroke="#fff" stroke-width="2"/></svg>
  <div class="hero-dots"><span class="on"></span><span></span><span></span><span></span></div>
</section>

<section class="services">
  <article class="service-card c1">
    <div class="card-head">
      <div class="card-icon"><svg width="14" height="12" viewBox="0 0 14 12"><rect x="1" y="1" width="12" height="8" fill="none" stroke="#fff" stroke-width="1.4"/><line x1="4" y1="11" x2="10" y2="11" stroke="#fff" stroke-width="1.4"/></svg></div>
      <h3 class="card-title">TECHNOLOGY CONSULTING</h3>
    </div>
    <div class="card-photo" role="img" aria-label="Consultants working together at a computer in an office"></div>
    <p class="card-text">We review your systems, map out risks and plan the right mix of hardware, software and services so your team works faster. Our consultants stay with you from first audit to final rollout and keep costs clear at every step along the way.</p>
    <a class="card-link" href="#">LEARN MORE</a>
  </article>

  <article class="service-card c2">
    <div class="card-head">
      <div class="card-icon"><svg width="14" height="12" viewBox="0 0 14 12"><rect x="2" y="1" width="10" height="4" fill="none" stroke="#fff" stroke-width="1.4"/><rect x="2" y="7" width="10" height="4" fill="none" stroke="#fff" stroke-width="1.4"/></svg></div>
      <h3 class="card-title">MANAGED IT SERVICES</h3>
    </div>
    <div class="card-photo" role="img" aria-label="Server room with racks of network equipment"></div>
    <p class="card-text">Our help desk watches your network day and night, patches servers, backs up data and fixes faults before they slow you down. One fixed monthly fee covers support, monitoring and regular reports so you always know how your systems are running.</p>
    <a class="card-link" href="#">LEARN MORE</a>
  </article>

  <article class="service-card c3">
    <div class="card-head">
      <div class="card-icon"><svg width="16" height="11" viewBox="0 0 16 11"><path d="M4 10h9a3 3 0 0 0 0-6 4 4 0 0 0-7.5-1A3.5 3.5 0 0 0 4 10z" fill="none" stroke="#fff" stroke-width="1.4"/></svg></div>
      <h3 class="card-title">CLOUD SERVICES &amp; HOSTING</h3>
    </div>
    <div class="card-photo" role="img" aria-label="Blue digital cloud network concept"></div>
    <p class="card-text">Move email, files and apps to a secure cloud hosted in local data centres. We handle migration, storage and backups, and scale your services up or down as the business grows, with fast support whenever you need a hand from our team.</p>
    <a class="card-link" href="#">LEARN MORE</a>
  </article>

  <article class="service-card c4">
    <div class="card-head">
      <div class="card-icon"><svg width="14" height="12" viewBox="0 0 14 12"><polyline points="4,2 1,6 4,10" fill="none" stroke="#fff" stroke-width="1.4"/><polyline points="10,2 13,6 10,10" fill="none" stroke="#fff" stroke-width="1.4"/></svg></div>
      <h3 class="card-title">SOFTWARE DEVELOPMENT</h3>
    </div>
    <div class="card-photo" role="img" aria-label="Developer writing code on a laptop screen"></div>
    <p class="card-text">We design and build custom web and mobile applications that fit the way you work. From early prototypes to testing and launch, our developers write clean code, connect your existing tools and keep improving the product after it goes live.</p>
    <a class="card-link" href="#">LEARN MORE</a>
  </article>
</section>

<section class="blog">
  <div class="blog-bg" role="img" aria-label="Dark photo of a workspace with a keyboard"></div>
  <div class="blog-content">
    <h2 class="blog-title">BLOG POSTS</h2>
    <p class="blog-text">Read our latest notes on cloud migration, network security and smart ways to get more from your IT budget. Our team shares practical tips, project stories and news from the industry every month to help your business stay ahead.</p>
    <a class="blog-link" href="#">LEARN MORE</a>
  </div>
  <svg class="blog-arrow prev" viewBox="0 0 12 20"><polyline points="10,2 3,10 10,18" fill="none" stroke="#fff" stroke-width="2"/></svg>
  <svg class="blog-arrow next" viewBox="0 0 12 20"><polyline points="2,2 9,10 2,18" fill="none" stroke="#fff" stroke-width="2"/></svg>
</section>

<footer class="site-footer">
  <nav class="footer-nav">
    <a href="#">HOME</a>
    <a href="#">ABOUT US</a>
    <a href="#">SERVICES</a>
    <a href="#">BLOG</a>
    <a href="#">CONTACT US</a>
  </nav>
  <div class="footer-info">
    <p>Copyright © 2015 Norvale Tech Group. All Rights Reserved</p>
    <p>Level 7, 48 Harbour Terrace, Southbank VIC 3006</p>
    <p>(03) 9000 1234</p>
  </div>
</footer>

</body>
</html>
```